Harbor Ladle is a modern and professional services business in the field of hospitality.

Need business card for a professional chef and consultant. Attention to detail and to stand out is our goal. I want a professional and stand out card which is not generic.
Would like a modern card with black gold or blue I’m not very sure on colours yet , open to ideas from those in the know. This is my second project and have been really happy with the process so far.
With 15 years in the hospitality industry I am launching into consulting and starting my own business. I’d like a few types of designs to look at which style I want. Open to suggestions. Thanks in advance for the work. I want something that will become part of my brand as it is launched. There is a chance for possible future work to the right person.

Target Market(s)

Restauranters and Registered training organisations.

Industry/Entity Type

Professional Service

Font styles to use
Serif

Colors

Designer to choose colors to be used in the design.

Requirements
Must have
• A stand out design, blue / black
Nice to have
• Can u get embossed cards?
Should not have
• Na

```html
<!DOCTYPE html>
<html lang="en">
<head>
<meta charset="utf-8">
<title>Harbor Ladle – Business Card</title>
<link href="https://fonts.googleapis.com/css2?family=PT+Serif:wght@400;700&display=swap" rel="stylesheet">
<style>
  :root {
    --backdrop: #d8d3cb;
    --card-dark: #070707;
    --card-mid: #161616;
    --card-light: #2b2b2b;
    --brand-blue: #14a9e6;
    --brand-blue-deep: #0a86bd;
    --text-light: #e9e9e9;
    --text-muted: #bdbdbd;
  }
  * { margin: 0; padding: 0; box-sizing: border-box; }
  html, body {
    width: 1200px;
    height: 900px;
    overflow: hidden;
    background: var(--backdrop);
    font-family: "PT Serif", Georgia, serif;
  }
  .business-card {
    position: absolute;
    left: 100px;
    top: 170px;
    width: 1000px;
    height: 560px;
    border-radius: 4px;
    background: linear-gradient(100deg, var(--card-dark) 0%, var(--card-mid) 55%, var(--card-light) 100%);
    box-shadow: 0 18px 40px rgba(0, 0, 0, 0.35);
  }
  .brand-tile {
    position: absolute;
    left: 190px;
    top: 200px;
    width: 240px;
    height: 150px;
    border-radius: 14px;
    background: linear-gradient(180deg, var(--brand-blue) 0%, var(--brand-blue-deep) 100%);
    display: flex;
    align-items: center;
    justify-content: center;
  }
  .brand-name {
    color: #ffffff;
    font-weight: 700;
    font-size: 30px;
    letter-spacing: 0.5px;
  }
  .divider {
    position: absolute;
    left: 520px;
    top: 130px;
    width: 2px;
    height: 300px;
    background: linear-gradient(180deg, var(--brand-blue) 0%, rgba(20, 169, 230, 0.15) 100%);
  }
  .contact-block {
    position: absolute;
    left: 550px;
    top: 120px;
    color: var(--text-light);
  }
  .holder-name {
    color: var(--brand-blue);
    font-weight: 700;
    font-size: 48px;
    line-height: 1;
  }
  .holder-role {
    color: var(--text-muted);
    font-size: 20px;
    margin-top: 4px;
  }
  .address {
    font-size: 22px;
    line-height: 1.15;
    margin-top: 42px;
  }
  .channels {
    list-style: none;
    margin-top: 34px;
    font-size: 22px;
    line-height: 1.3;
  }
  .channel-key {
    display: inline-block;
    width: 24px;
    color: var(--brand-blue);
    font-weight: 700;
  }
</style>
</head>
<body>
  <div class="business-card">
    <div class="brand-tile">
      <span class="brand-name">Harbor Ladle</span>
    </div>
    <div class="divider"></div>
    <div class="contact-block">
      <div class="holder-name">Harbor Ladle</div>
      <div class="holder-role">Managing Member</div>
      <div class="address">28 Quayside Row,<br>Port Street, CA 90412</div>
      <ul class="channels">
        <li><span class="channel-key">T</span> - (555) 214-3097</li>
        <li><span class="channel-key">E</span> - hello@harborladle.com</li>
        <li><span class="channel-key">W</span> - www.harborladle.com</li>
      </ul>
    </div>
  </div>
</body>
</html>
```